Brochure Design Project

A4 Portrait
8 Page Sales brochure for Automatic Coffee Machines for Offices.
We have 4 products in 4 cateries.
Small Office
Medium Office
Large Office
Whole Company / Food Service.

There will be a product image plus 3-4 accessories for each product

Then a brief sales pitch text for each product.

We supply to public listed companies therefore it has to be professional, well presented and eye catching.

Thank you
Updates

I will make the budget $200

Hello,

Please note that I've made changes to the job brief. 

Thanks

Walter 

Hi 

Please find attached contents in pdf for your implementation.

1. Small Office Solution
2. Medium Office Solution 
3. Large Office Solution
4. Whole Company Solution
5. Food Service

Thanks 

Walter

Hi All

Budget increased to $200, extended project by 7 more days.

Thank you

Harold Bensu

Target Market(s)

Big Corporate Companies in major Australian cities

Industry/Entity Type

It Company

Requirements
Must have
• A4 Portrait
8 Page photo and sales pitch text. One product per page starting from 3nd page
5 products into 5 categories of

Page 2 will tell about our company and services

Small Office Solution (page 3)
$16 per day)

Medium Office Solution (page 4)
$18 per day)

Large Office Solution (page 5)
$19 per day)

Whole Company (page 6)
$24 per day)

Food Service Solution (page 7
$28 per day

Each product page will highlight
eg
Small Office Solution
$16 per day)

Each page will have 3-4 accessories (photos)

Page 8 Our logo, address & Conatct details - Please see for contact details http://www.brewnova.com.au/brew_nova
Nice to have
• Logo, photo of coffee machine, an office environment where people are kind of enjoying coffee in a lounge.

Should not have
• Not messy, no old style,

```html
<!DOCTYPE html>
<html lang="en">
<head>
<meta charset="utf-8">
<title>Brew Nova – Automatic Coffee Machines Brochure Cover</title>
<link href="https://fonts.googleapis.com/css2?family=Arimo:wght@400;700&display=swap" rel="stylesheet">
<style>
  :root {
    --stage: #f6f7f7;
    --paper: #ffffff;
    --brand-red: #e3151f;
    --brand-red-deep: #c80f18;
    --ink: #2b2b2b;
    --ink-soft: #4a4a4a;
    --photo-light: #dfe6ea;
    --photo-mid: #a9b4bb;
    --machine-dark: #2c2f33;
    --machine-steel: #b9bec3;
  }
  * { margin: 0; padding: 0; box-sizing: border-box; }
  html, body {
    width: 1200px;
    height: 900px;
    overflow: hidden;
    background: var(--stage);
    font-family: "Arimo", Arial, sans-serif;
  }
  .canvas {
    position: relative;
    width: 1200px;
    height: 900px;
  }
  .cover {
    position: absolute;
    left: 303px;
    top: 30px;
    width: 594px;
    height: 840px;
    background: var(--paper);
    box-shadow: 0 6px 22px rgba(0,0,0,0.18);
    overflow: hidden;
  }
  .cover-art {
    position: absolute;
    inset: 0;
    width: 594px;
    height: 840px;
  }
  .brand-mark {
    position: absolute;
    right: 40px;
    top: 258px;
    display: flex;
    align-items: center;
    gap: 10px;
    color: var(--paper);
    font-size: 26px;
    font-weight: 400;
    letter-spacing: 0.3px;
  }
  .brand-mark .dot {
    width: 14px;
    height: 14px;
    border-radius: 50%;
    background: var(--paper);
  }
  .machine-photo {
    position: absolute;
    left: 70px;
    top: 372px;
    width: 230px;
    height: 190px;
    border-radius: 4px;
    background: linear-gradient(90deg, var(--machine-steel) 0%, var(--machine-dark) 45%, var(--machine-steel) 100%);
    box-shadow: 0 8px 14px rgba(0,0,0,0.25);
  }
  .cover-title {
    position: absolute;
    left: 140px;
    top: 600px;
    color: var(--ink);
  }
  .cover-title .brand-name {
    color: var(--brand-red);
    font-size: 20px;
    font-weight: 700;
  }
  .cover-title .headline {
    font-size: 24px;
    font-weight: 700;
    line-height: 1.15;
  }
  .cover-title .subline {
    font-size: 15px;
    font-weight: 700;
    color: var(--ink-soft);
  }
</style>
</head>
<body>
<div class="canvas">
  <section class="cover">
    <svg class="cover-art" viewBox="0 0 594 840" xmlns="http://www.w3.org/2000/svg">
      <defs>
        <linearGradient id="officePhotoTone" x1="0" y1="0" x2="1" y2="1">
          <stop offset="0" stop-color="#eef2f4"/>
          <stop offset="0.55" stop-color="#b8c2c8"/>
          <stop offset="1" stop-color="#6f7a82"/>
        </linearGradient>
      </defs>
      <rect class="office-photo" role="img" aria-label="Photo of two colleagues laughing over coffee in a bright office" x="0" y="0" width="594" height="340" fill="url(#officePhotoTone)"/>
      <path class="swoosh-band" d="M0,300 Q300,240 594,228 L594,352 Q320,340 0,430 Z" fill="var(--brand-red)"/>
      <path class="swoosh-line" d="M0,318 Q300,262 594,250" fill="none" stroke="#ffffff" stroke-width="5"/>
      <path class="swoosh-shadow" d="M0,430 Q320,340 594,352 L594,362 Q320,352 0,440 Z" fill="var(--brand-red-deep)" opacity="0.5"/>
      <path class="accent-stripe" d="M300,470 Q460,400 594,420 L594,444 Q460,428 310,486 Z" fill="var(--brand-red)"/>
      <path class="footer-line" d="M60,745 Q320,720 594,690" fill="none" stroke="var(--brand-red)" stroke-width="5"/>
      <path class="footer-band" d="M0,790 Q300,762 594,725 L594,840 L0,840 Z" fill="var(--brand-red)"/>
      <path class="footer-gap" d="M0,804 Q300,778 594,742" fill="none" stroke="#ffffff" stroke-width="4"/>
    </svg>

    <div class="brand-mark"><span class="dot"></span><span>Brew Nova</span></div>

    <div class="machine-photo" role="img" aria-label="Product photo of an automatic coffee machine with cup warmer"></div>

    <div class="cover-title">
      <p class="brand-name">Brew Nova</p>
      <h1 class="headline">Automatic Coffee Machines</h1>
      <p class="subline">for Commercial Offices and Cafes</p>
    </div>
  </section>
</div>
</body>
</html>
```